LABEL DESIGNS FOR SKINCARE LINE

Hello we are needing 12 label various label designs but would like to see you design ONE. We will pick winner from this and send the rest.
LABEL SIZE -2x7
JAR SIZE IS - 8oz
LOGOS FILES BELOW
https://files.pavorna-share.net/drive/folders/7xk3q-wumTrazPLoqVnnRTZBKHAE2DpLW
INFORMATION FOR LABEL
Calm Dune Hush Whipped Body Sugar Scrub 8oz
Ideal for all Skin Types
Ingredients:
Pure Cane Sugar, Extra Virgin Coconut Oil, Mango Butter, Kukum Butter, Emulsifying Wax, Jojoba Seed Oil, Sweet Almond Oil, Strawberry Essential Oil, and Pomegranate Essential Oil.
Directions to use Body Sugar Scrub:
Apply to wet skin gently in a circular motion on desired body area, hands, feet, legs, arms, etc. Once you have a good scrub, rinse, pat dry, and enjoy soft, hydrated skin. Best to use in the shower. Use between 2-3 times a week if needed.
*Cautions:
(1) Allergy: Approach this product with extreme caution, if you have allergies
(2) Avoid direct contact with eyes
Storage/Shelf Life of Product:
For best results, stir/mix scrub with the wooden or plastic spoon before each use. The shelf life of all sugar scrubs is 6-8 weeks. Keep the product in a cool, dry place, away from hot or heated temperatures.
All Natural, Cruelty-Free, Vegan Free
No Mineral Oil
No Petroleum
No Parabens

```html
<!DOCTYPE html>
<html lang="en">
<head>
<meta charset="utf-8">
<title>Calm Dune Hush — Whipped Body Sugar Scrub Label</title>
<link rel="stylesheet" href="https://fonts.googleapis.com/css2?family=Bodoni+Moda:opsz,wght@6..96,500;6..96,700&family=Montserrat:wght@400&display=swap">
<style>
  :root {
    --canvas: #ffffff;
    --dieline: #1f1f1f;
    --berry: #e65176;
    --berry-deep: #e0436b;
    --star-tint: #fbe3ea;
    --paper: #ffffff;
    --ink: #1c1c1c;
  }
  * { box-sizing: border-box; margin: 0; padding: 0; }
  html, body {
    width: 1200px;
    height: 1200px;
    overflow: hidden;
    background: var(--canvas);
  }
  .label-sheet {
    position: absolute;
    left: 70px;
    top: 448px;
    width: 1061px;
    height: 304px;
    border: 2px solid var(--dieline);
  }
  .label-art {
    position: absolute;
    left: 313px;
    top: 0;
    width: 432px;
    height: 100%;
  }
  .brand-band {
    position: absolute;
    left: 0;
    top: 0;
    width: 100%;
    height: 105px;
    background: radial-gradient(circle at 50% 50%, var(--paper) 0%, var(--star-tint) 140%);
  }
  .brand-name {
    position: absolute;
    left: 0;
    top: 0;
    width: 100%;
    height: 105px;
    display: flex;
    align-items: center;
    justify-content: center;
    font-family: "Bodoni Moda", serif;
    font-weight: 700;
    font-size: 36px;
    color: var(--berry-deep);
    letter-spacing: 0.5px;
  }
  .product-band {
    position: absolute;
    left: 0;
    top: 105px;
    width: 100%;
    height: 197px;
    background: var(--berry);
    color: var(--paper);
  }
  .product-name {
    position: absolute;
    left: 0;
    top: 8px;
    width: 100%;
    text-align: center;
    font-family: "Bodoni Moda", serif;
    font-weight: 500;
    font-size: 56px;
    line-height: 47px;
    letter-spacing: -1.5px;
  }
  .product-type {
    position: absolute;
    left: 0;
    top: 126px;
    width: 100%;
    text-align: center;
    font-family: "Montserrat", sans-serif;
    font-weight: 400;
    font-size: 17px;
    color: var(--ink);
  }
  .net-weight {
    position: absolute;
    left: 41px;
    top: 170px;
    font-family: "Montserrat", sans-serif;
    font-weight: 400;
    font-size: 16px;
    color: var(--paper);
  }
</style>
</head>
<body>
  <div class="label-sheet">
    <div class="label-art">
      <div class="brand-band" role="img" aria-label="Pattern of small pink sparkle stars on white"></div>
      <div class="brand-name">Sugar Lark</div>
      <div class="product-band">
        <h1 class="product-name">Calm Dune<br>Hush</h1>
        <p class="product-type">Whipped Body Sugar Scrub</p>
        <p class="net-weight">8oz</p>
      </div>
    </div>
  </div>
</body>
</html>
```